New banner graphics for Kelbro.com website

I've developed a software tool that helps businesses ensure they are working on their most valuable and important work.

I would like a banner graphic for my home page (www.kelbro.com) that can somehow capture the value of focus and intentional outcomes.

I had an initial thought of a starry sky that shifts focus to a few bright stars, but while that might sound ok, I think my idea is lame hence I'm coming to you guys.

My sites two primary colors are a soft purple and gray.
#919EC1(purple)
#9E9E9E (gray)

Target Market(s)

B2B for enterprises. Typical customers are CFOs, CIOs/Heads of IT

Industry/Entity Type

Business Software

Number of Pages Required

1 page

Font styles to use
Sans Serif

Colors
b8a6cd
cedeed

Requirements
Must have
• I use Divi as my Wordpress theme and the current main landing page can be seen at www.kelbro.com.
• My logo colors are:
• #919EC1(purple)
• #9E9E9E (gray)
Should not have
• Lots of distraction or visual "noise". I want to re-enforce the message that my software is focused on their business and not my products or website.

```html
<!DOCTYPE html>
<html lang="en">
<head>
<meta charset="utf-8">
<title>Kelbro – Keystone</title>
<link rel="stylesheet" href="https://fonts.googleapis.com/css2?family=Lato:wght@300;400;700&display=swap">
<style>
:root{
  --purple:#b8a6cd;
  --purple-deep:#9d89b8;
  --brand-purple:#919ec1;
  --gray:#9e9e9e;
  --text:#5d5d66;
  --text-light:#8a8a92;
  --mint:#e3efee;
  --soft-gray:#f4f4f6;
  --white:#ffffff;
  --night-1:#1c2436;
  --night-2:#3d4a66;
  --night-3:#6b6f86;
}
*{box-sizing:border-box;margin:0;padding:0}
html,body{width:1200px;height:3252px;overflow:hidden}
body{font-family:"Lato",Arial,sans-serif;color:var(--text);background:var(--white)}
.btn{display:inline-block;font-size:15px;letter-spacing:1px;padding:12px 32px;border-radius:4px;text-transform:uppercase}
.btn-solid{background:var(--purple);color:var(--white)}
.btn-outline{border:2px solid var(--purple);color:var(--purple-deep);background:var(--white)}

/* header */
.site-header{height:72px;display:flex;align-items:center;justify-content:space-between;padding:0 28px 0 22px;border-bottom:1px solid #eee}
.brand{font-size:30px;font-weight:300;color:var(--brand-purple);letter-spacing:1px}
.main-nav{display:flex;gap:44px;align-items:center;font-size:14px;color:#555;letter-spacing:.5px}
.main-nav svg{display:block}

/* hero */
.hero{position:relative;height:588px;color:var(--white);text-align:center;overflow:hidden}
.hero-photo{position:absolute;inset:0;background:linear-gradient(180deg,var(--night-1) 0%,var(--night-2) 45%,var(--night-3) 72%,#24242c 100%)}
.hero-ridge{position:absolute;left:0;right:0;bottom:0;height:170px;background:linear-gradient(180deg,rgba(20,20,26,0) 0%,#15151b 60%)}
.hero-content{position:relative;padding-top:180px}
.hero h1{font-size:62px;font-weight:400;letter-spacing:.5px}
.hero p{font-size:24px;font-weight:300;margin-top:8px}
.hero .btn{margin-top:30px}
.hero-arrow{position:absolute;top:320px;font-size:30px;color:rgba(255,255,255,.6)}

/* keystone intro */
.intro{height:640px;text-align:center;padding-top:70px}
.intro-ornament{width:220px;height:30px;margin:0 auto;background:linear-gradient(180deg,rgba(196,196,204,0) 0%,rgba(196,196,204,.35) 100%);border-radius:4px}
.intro h2{font-size:42px;font-weight:300;color:#666;margin-top:6px}
.intro .tagline{font-size:24px;font-weight:300;color:var(--text-light);margin-top:14px}
.intro .lead{font-size:15px;line-height:1.6;color:var(--text-light);width:600px;margin:18px auto 0}
.features{display:flex;justify-content:center;gap:70px;margin-top:46px}
.feature{width:140px;color:var(--purple-deep);font-size:18px;line-height:1.3}
.feature svg{display:block;margin:0 auto 14px}
.intro .btn{margin-top:46px}

/* value */
.value{height:500px;background:var(--mint);display:flex;align-items:center;padding:0 120px 0 230px;gap:80px}
.monitor{flex:none;width:330px}
.monitor .screen{height:200px;border:10px solid #2b2b30;border-radius:6px;background:linear-gradient(135deg,#e8e8ee,#b9b3c6 60%,#8f8aa0)}
.monitor .stand{width:60px;height:36px;margin:0 auto;background:#c9c9cf}
.monitor .base{width:130px;height:6px;margin:0 auto;background:#b5b5bc;border-radius:3px}
.value-copy h3{font-size:32px;font-weight:300;color:#666}
.value-copy p{font-size:14px;line-height:1.65;color:var(--text-light);margin-top:18px}

/* testimonials */
.testimonials{height:410px;padding-top:46px;text-align:center}
.testimonials h2{font-size:36px;font-weight:300;color:#666;border-bottom:1px solid #ddd;display:inline-block;padding:0 40px 12px}
.quotes{display:flex;justify-content:center;gap:60px;margin-top:42px;text-align:left}
.quote{width:290px}
.quote p{font-size:15px;line-height:1.6;color:var(--text);border-left:2px solid #ddd;padding-left:16px;height:130px}
.author{display:flex;align-items:center;gap:14px;margin-top:20px}
.avatar{width:46px;height:46px;border-radius:50%;background:linear-gradient(135deg,#c8c2d2,#8c8799)}
.author strong{display:block;font-size:12px;color:#666;font-weight:700;text-transform:uppercase}
.author span{font-size:11px;color:var(--text-light)}

/* difference */
.difference{height:770px;background:var(--soft-gray);text-align:center;padding-top:80px}
.difference h2{font-size:36px;font-weight:300;color:#666}
.pillars{display:flex;justify-content:center;gap:60px;margin-top:56px}
.pillar{width:200px}
.pillar .badge{width:120px;height:120px;border-radius:50%;background:var(--purple);margin:0 auto;display:flex;align-items:center;justify-content:center}
.pillar h4{font-size:24px;font-weight:400;color:#555;margin-top:24px;line-height:1.2;min-height:58px}
.pillar p{font-size:13px;line-height:1.6;color:var(--text-light);margin:14px auto 0;width:170px}
.difference .btn{margin-top:60px}

/* footer */
.site-footer{height:272px;background:var(--purple);color:var(--white);padding:54px 100px 0}
.footer-cols{display:flex;gap:70px}
.footer-cols h5{font-size:14px;letter-spacing:1px;text-transform:uppercase;font-weight:400;margin-bottom:16px}
.links{display:grid;grid-template-columns:130px 130px;gap:8px 20px;font-size:13px}
.contact{width:280px;font-size:13px;line-height:1.9}
.signup{width:360px;font-size:13px}
.signup form{display:flex;margin-top:10px}
.signup .field{flex:1;height:34px;background:var(--white);border-radius:3px 0 0 3px}
.signup .send{background:var(--purple-deep);padding:0 18px;line-height:34px;font-size:12px;letter-spacing:1px;border-radius:0 3px 3px 0}
.social{display:flex;gap:12px;margin-top:18px;justify-content:center}
.social span{width:30px;height:30px;border-radius:50%;background:var(--white)}
.legal{border-top:1px solid rgba(255,255,255,.4);margin-top:36px;padding-top:14px;font-size:11px;display:flex;justify-content:space-between}
</style>
</head>
<body>

<header class="site-header">
  <div class="brand">kelbro</div>
  <nav class="main-nav">
    <span>REQUEST A DEMO</span>
    <span>LINKS ⌄</span>
    <span>START NOW</span>
    <svg width="14" height="14" viewBox="0 0 14 14" fill="none" stroke="#888" stroke-width="1.6"><circle cx="6" cy="6" r="4.5"/><path d="M9.5 9.5 13 13"/></svg>
  </nav>
</header>

<section class="hero">
  <div class="hero-photo" role="img" aria-label="Photo of a starry night sky above a rocky ridge with a lone figure seated on the rocks"></div>
  <div class="hero-ridge"></div>
  <span class="hero-arrow" style="left:20px">‹</span>
  <span class="hero-arrow" style="right:20px">›</span>
  <div class="hero-content">
    <h1>Is Your Business Strategy</h1>
    <p>Be confident that you’re focused on your most valuable work.</p>
    <span class="btn btn-solid">Start Now !</span>
  </div>
</section>

<section class="intro">
  <div class="intro-ornament" role="img" aria-label="Decorative swoosh ornament above the heading"></div>
  <h2>Get KEYSTONE</h2>
  <p class="tagline">a simple software tool that makes your business goals actionable</p>
  <p class="lead">Even if you’ve never felt comfortable defining your business strategy, Keystone is for you. It’s simple to use, easy to understand, and keeps you focused on outcomes.</p>
  <div class="features">
    <div class="feature">
      <svg width="60" height="46" viewBox="0 0 60 46" fill="none" stroke="#9d89b8" stroke-width="3"><path d="M4 44h52"/><rect x="8" y="26" width="9" height="16"/><rect x="25" y="16" width="9" height="26"/><rect x="42" y="6" width="9" height="36"/></svg>
      Define the Outcomes</div>
    <div class="feature">
      <svg width="60" height="46" viewBox="0 0 60 46" fill="none" stroke="#9d89b8" stroke-width="3"><path d="M30 4v40"/><path d="M12 8h30l6 5-6 5H12z"/><path d="M48 22H20l-6 5 6 5h28z"/></svg>
      Get the Direction</div>
    <div class="feature">
      <svg width="60" height="46" viewBox="0 0 60 46" fill="#9d89b8"><circle cx="30" cy="12" r="8"/><path d="M16 42c0-10 6-16 14-16s14 6 14 16z"/><circle cx="12" cy="18" r="5"/><circle cx="48" cy="18" r="5"/></svg>
      Focus the Resources</div>
    <div class="feature">
      <svg width="60" height="46" viewBox="0 0 60 46" fill="none" stroke="#9d89b8" stroke-width="3"><path d="M4 44h52"/><path d="M8 8 22 20l10-6 18 22"/><path d="M42 36h8v-8"/></svg>
      Reduce the Risk</div>
    <div class="feature">
      <svg width="60" height="46" viewBox="0 0 60 46" fill="#9d89b8"><circle cx="30" cy="8" r="6"/><circle cx="14" cy="20" r="5"/><circle cx="46" cy="20" r="5"/><path d="M20 42c0-10 4-16 10-16s10 6 10 16z"/><path d="M5 42c0-8 4-12 9-12s9 4 9 12z"/><path d="M37 42c0-8 4-12 9-12s9 4 9 12z"/></svg>
      Increase Team Engagement</div>
  </div>
  <span class="btn btn-outline">Start Now</span>
</section>

<section class="value">
  <div class="monitor">
    <div class="screen" role="img" aria-label="Screenshot of a business planning video on a desktop monitor"></div>
    <div class="stand"></div>
    <div class="base"></div>
  </div>
  <div class="value-copy">
    <h3>The Kelbro Strategic Value</h3>
    <p>Most organisations work on too many ideas at once. Our approach turns your business goals into a short list of outcomes, so every team knows what matters and why it matters today.</p>
    <p>Keystone links every project back to the outcomes you chose. Leaders see progress at a glance, spend less time in status meetings, and move resources to the work that returns the most value.</p>
    <p>No consultants, no thick binders. Just a clear plan your people can follow and update as the market shifts around you.</p>
  </div>
</section>

<section class="testimonials">
  <h2>What people are saying...</h2>
  <div class="quotes">
    <div class="quote">
      <p>Keystone brings the fast world of strategic planning down to earth, and fits the practical needs of modern agile teams.</p>
      <div class="author"><div class="avatar" role="img" aria-label="Portrait photo placeholder"></div><div><strong>Dana Ruiz</strong><span>CEO, Northfield Group</span></div></div>
    </div>
    <div class="quote">
      <p>This software helps me with the conversation I have with my peers around what really matters for our business and what’s not.</p>
      <div class="author"><div class="avatar" role="img" aria-label="Portrait photo placeholder"></div><div><strong>Owen Hale</strong><span>CIO, Alder Bay</span></div></div>
    </div>
    <div class="quote">
      <p>I wish we would have had something like this as we moved from our recent consulting engagement instead of just the slide deck we received. We would still be using it.</p>
      <div class="author"><div class="avatar" role="img" aria-label="Portrait photo placeholder"></div><div><strong>Nina Park</strong><span>VP Finance, Corvane Labs</span></div></div>
    </div>
  </div>
</section>

<section class="difference">
  <h2>What Makes Keystone Different?</h2>
  <div class="pillars">
    <div class="pillar">
      <div class="badge"><svg width="54" height="54" viewBox="0 0 54 54" fill="none" stroke="#fff" stroke-width="6" stroke-linecap="round" stroke-linejoin="round"><path d="M10 28l11 11 23-24"/></svg></div>
      <h4>Ease of Use</h4>
      <p>We want you to spend time thinking about your goals, not learning yet another tool. Keystone has a modern way of making it more intuitive.</p>
    </div>
    <div class="pillar">
      <div class="badge"><svg width="54" height="54" viewBox="0 0 54 54" fill="none" stroke="#fff" stroke-width="4" stroke-linecap="round"><path d="M27 8a13 13 0 0 0-8 23v6h16v-6a13 13 0 0 0-8-23z"/><path d="M21 43h12M23 48h8"/></svg></div>
      <h4>Practical Approach</h4>
      <p>We want you to spend time planning for your organisation’s success, not decoding theory. Keystone keeps every step simple and useful.</p>
    </div>
    <div class="pillar">
      <div class="badge"><svg width="54" height="54" viewBox="0 0 54 54" fill="#fff"><rect x="8" y="30" width="9" height="16"/><rect x="22" y="20" width="9" height="26"/><rect x="36" y="10" width="9" height="36"/></svg></div>
      <h4>Focus on Outcomes</h4>
      <p>We want you to measure results, not activity. Keystone ties each task to the outcome it serves so progress is easy to see.</p>
    </div>
    <div class="pillar">
      <div class="badge"><svg width="54" height="54" viewBox="0 0 54 54" fill="none" stroke="#fff" stroke-width="5"><circle cx="21" cy="21" r="9"/><circle cx="37" cy="36" r="7"/><path d="M21 6v6M21 30v6M6 21h6M30 21h6M37 24v4M37 44v4M25 36h4M45 36h4"/></svg></div>
      <h4>Support of Industry Frameworks</h4>
      <p>We want you to keep the methods you trust. Keystone works alongside common planning frameworks without extra effort.</p>
    </div>
  </div>
  <span class="btn btn-outline">Start Now</span>
</section>

<footer class="site-footer">
  <div class="footer-cols">
    <div>
      <h5>Quick Links</h5>
      <div class="links"><span>Resources</span><span>Terms of Service</span><span>Contact Us</span><span>Pricing</span><span>Support</span><span>About</span><span>FAQ</span></div>
    </div>
    <div class="contact">
      <h5>Contact Info</h5>
      <div>Kelbro, 48 Harbor Lane, Suite 210</div>
      <div>Westbrook, ON Canada</div>
      <div>+1 555 010 4827</div>
      <div>hello@kelbro.com</div>
    </div>
    <div class="signup">
      <h5>Sign up for Newsletters</h5>
      <div>Please sign up for the latest news</div>
      <form><span class="field"></span><span class="send">SUBSCRIBE</span></form>
      <div class="social"><span></span><span></span><span></span></div>
    </div>
  </div>
  <div class="legal"><span>© 2016 KELBRO · All rights reserved · Terms of Use</span><span>www.kelbro.com</span></div>
</footer>

</body>
</html>
```